zQuandaro Marketing - SEM, Influencer website. FUN RETRO VIBES.

I included content. Need an advertising website that displays, my services, blog and about me and contact.
I need to be able to easily update content, blogs by myself. Need it to be a Wordpress. I included some content pages. Please let me know if this give a better idea of what I do and the tone I am looking for.
Target Market(s)
Small Business Entrepreneurs, Start-ups, Male and Female ages 25-50
Industry/Entity Type
Advertising
Coding
Coded - Design and coding required
Number of Pages Required
3 page
Font styles to use
Other font styles liked:
- Lazer 64
Requirements
Must have
- Services, Blog, About Me, Contact. Creative Design is really what I want. Unique and fun imagery. I like the 80's style of design. Retro colors, in the logo. LAzer 84 font is cool. Hex colors should be in the brief. MUST LOOK GOOD ON MOBILE. The mobile experience has to be good.
Nice to have
- I am open minded to new creative ideas.
Hex Code
#000205
#3978A3
#5BF8FB
#7B7BFB
#5CC9EC
#AB63FA
Should not have
- Cookie Cutter feel. They made me choose the color wheel but the colors I want are on the brief. Please let me know if you need more logo images, images of me

```html
<!DOCTYPE html>
<html lang="en">
<head>
<meta charset="utf-8">
<title>zQuandaro Marketing – Digital Advertising</title>
<link href="https://fonts.googleapis.com/css2?family=Lato:wght@300;400;700&family=Oswald:wght@500&family=Permanent+Marker&display=swap" rel="stylesheet">
<style>
:root{
  --ink:#000205;
  --blue:#3978A3;
  --cyan:#5BF8FB;
  --periwinkle:#7B7BFB;
  --sky:#5CC9EC;
  --violet:#AB63FA;
  --plum:#8B68C4;
  --page:#e4e4e4;
  --panel:#f3f3f3;
  --text:#7a7a7a;
  --footer:#3b3b3d;
  --retro:'Permanent Marker', cursive;
  --body:'Lato', sans-serif;
}
*{margin:0;padding:0;box-sizing:border-box}
html,body{width:1200px;height:3526px;overflow:hidden}
body{background:var(--page);font-family:var(--body);color:var(--text);position:relative}
.abs{position:absolute}
.retro{font-family:var(--retro);font-style:normal;transform:skewX(-10deg);letter-spacing:1px}

/* header */
.topbar{left:0;top:0;width:1200px;height:49px;background:var(--ink)}
.site-tag{left:0;top:10px;width:1200px;text-align:center;color:var(--violet);font-size:22px}
.navbar{left:0;top:49px;width:1200px;height:36px;background:var(--violet)}
.nav{left:449px;top:49px;height:36px;display:flex;gap:22px;align-items:center;list-style:none}
.nav li{color:#fff;font-size:13px}
.badge{left:176px;top:0;width:184px;height:154px}
.badge-name{left:176px;top:96px;width:184px;text-align:center;color:#d9c6ff;font-size:20px;font-weight:300;letter-spacing:1px}
.hero{left:0;top:85px;width:1200px;height:343px;
  background:radial-gradient(ellipse at 50% 60%,rgba(255,255,255,.55) 0,rgba(255,255,255,0) 45%),
  linear-gradient(90deg,#9a68f0 0%,#6fa6f0 30%,#c48be0 55%,#7bc0ef 80%,#a872f2 100%)}
.hero-title{left:0;top:178px;width:1200px;text-align:center;color:#fff;font-size:52px}
.hero-sub{left:0;top:268px;width:1200px;text-align:center;color:#fff;font-size:20px;font-weight:300}
.hero-steps{left:0;top:343px;width:1200px;text-align:center;color:#fff;font-size:16px;font-weight:700;letter-spacing:6px}

/* banners */
.banner{height:159px;overflow:hidden}
.banner-photo{position:absolute;left:0;top:0;height:159px}
.banner-word{position:absolute;color:#fff;font-size:44px;top:48px}

/* visualize */
.visualize{left:124px;top:477px;width:947px;height:552px;background:#fff}
.visualize .banner{background:linear-gradient(90deg,#c79cf7 0%,var(--violet) 45%,#b57af9 100%)}
.visualize .banner-photo{width:300px;background:linear-gradient(120deg,#2d2a33,#c9a77d 55%,#e6e1ea)}
.visualize .col-left{position:absolute;left:0;top:159px;width:524px;height:393px;padding:74px 33px 0}
.visualize .col-right{position:absolute;left:524px;top:159px;width:423px;height:393px;background:var(--panel);padding:32px 0 0 32px}
.lede{color:var(--violet);font-size:19.5px;line-height:24px;font-weight:400;margin-bottom:24px}
.lede span{color:var(--sky)}
.copy{font-size:13px;line-height:18px;font-weight:300;color:#808080;margin-bottom:18px}
.ticks{list-style:none}
.ticks li{position:relative;padding-left:19px}
.ticks li::before{content:"✓";position:absolute;left:0;top:0}
.vis-list li{font-size:13.5px;line-height:23.3px;color:#888;font-weight:300}
.vis-list li::before{color:var(--sky)}
.vis-list li.wrap{line-height:18px;padding-top:3px;padding-bottom:3px}

/* plan */
.plan{left:124px;top:1083px;width:947px;height:613px}
.plan .banner{position:relative;background:linear-gradient(90deg,#8fdcf3 0%,#67cdee 55%,#5ec9ed 100%)}
.plan .banner-photo{width:650px;background:linear-gradient(90deg,#2f3a46 0%,#7e8e9c 45%,#d8e2e8 80%,rgba(216,226,232,0) 100%)}
.plan .banner-word{color:var(--blue);right:40px}
.plan .col-left{position:absolute;left:0;top:159px;width:553px;height:454px;background:var(--blue);padding:62px 33px 0;color:#fff}
.plan .col-right{position:absolute;left:553px;top:159px;width:394px;height:454px;background:var(--periwinkle);padding:62px 0 0 38px}
.plan h2{font-size:19.5px;line-height:24px;font-weight:400;color:var(--sky);text-transform:uppercase}
.plan h2 b{color:#fff;font-weight:400}
.plan .copy{color:#fff;font-size:12px;line-height:16px;margin:24px 0 50px}
.resource-grid{display:grid;grid-template-columns:222px 260px;margin-top:24px}
.resource-grid li{font-size:12.5px;line-height:20px;color:#fff;font-weight:300;padding-left:14px}
.plan-list li{font-size:13.5px;line-height:28px;color:#fff;padding-left:16px}

/* execute */
.execute{left:130px;top:1754px;width:945px;height:510px;background:#fff}
.execute .banner{position:relative;background:var(--ink)}
.execute .banner-photo{width:640px;background:linear-gradient(90deg,#e9e9ea 0%,#3f4f63 25%,#27344a 60%,var(--ink) 100%)}
.execute .banner-word{right:30px}
.execute .col-left{position:absolute;left:0;top:159px;width:562px;height:351px;padding:50px 30px 0 30px}
.execute .col-right{position:absolute;left:562px;top:159px;width:383px;height:351px;background:var(--panel);padding:95px 0 0 44px}
.execute h2{font-size:19.5px;line-height:22px;color:var(--ink);font-weight:400;text-transform:uppercase;margin-bottom:24px}
.execute .copy{font-size:15px;line-height:20px;margin-bottom:20px}
.cta{display:inline-flex;align-items:center;gap:30px;margin-top:22px;margin-left:-4px;border:2px solid var(--ink);height:48px;padding:0 18px 0 20px;font-size:13px;color:var(--ink);font-weight:400;width:334px}
.exe-list li{font-size:14px;line-height:28px;color:#888;font-weight:300;padding-left:22px}
.exe-list li::before{color:var(--blue)}

/* mission */
.mission{left:119px;top:2312px;width:947px;height:333px;background:#fff}
.statement{position:absolute;top:71px;width:349px;height:192px;padding:8px}
.statement .frame{height:100%;border:2px solid #fff;text-align:center;color:#fff;padding:28px 22px 0}
.statement h3{font-family:'Oswald',sans-serif;font-weight:500;font-size:23px;margin-bottom:16px}
.statement p{font-size:16.5px;font-weight:700;line-height:23px}
.statement.mission-box{left:75px;background:var(--blue)}
.statement.purpose-box{left:546px;background:var(--plum)}

/* partners */
.partners{left:119px;top:2695px;width:947px;height:334px;background:#fff}
.brand{position:absolute;display:flex;align-items:center;gap:12px;color:#8a8a8a;font-size:26px;font-weight:300;line-height:26px}
.brand .dot{width:58px;height:58px;background:#f5a623;flex:none}
.dashboard{position:absolute;left:259px;top:21px;width:177px;height:95px;background:linear-gradient(180deg,#f2f4f7,#dde6ef)}
.ad-badge{position:absolute;left:776px;top:36px;width:142px;height:71px;background:#3b5998}
.partner-copy{position:absolute;font-size:15px;line-height:19px;color:#8a8a8a;font-weight:300}
.partner-copy p{margin-bottom:19px}

/* share */
.share-title{left:0;top:3068px;width:1200px;text-align:center;color:var(--violet);font-size:31px}
.share-row{left:527px;top:3136px;display:flex;gap:3px}
.share-row span{width:29px;height:29px;display:block}
.share-row .plus{width:50px;background:#f0503c;color:#fff;font-size:18px;line-height:27px;padding-left:7px;font-weight:700}

/* footer */
.footer{left:0;top:3215px;width:1200px;height:209px;background:var(--footer)}
.foot-name{left:126px;top:3285px;width:272px;text-align:center;color:var(--violet);font-size:34px;font-weight:300;letter-spacing:1px}
.foot-steps{left:126px;top:3340px;width:272px;text-align:center;color:#fff;font-size:13px;font-weight:700;letter-spacing:4.5px}
.quick-title{left:456px;top:3256px;color:var(--violet);font-size:16px;font-weight:700}
.quick{left:460px;top:3286px;list-style:none}
.quick li{color:#fff;font-size:12.5px;line-height:27px}
.news-label{left:620px;top:3293px;color:#fff;font-size:13px}
.news-input{left:793px;top:3286px;width:199px;height:31px;background:#fff;border:1px solid #ccc}
.news-btn{left:1003px;top:3286px;width:61px;height:31px;background:var(--violet);color:#fff;font-size:13px;text-align:center;line-height:31px}
.social{left:856px;top:3340px;display:flex;gap:6px}
.social span{width:36px;height:36px;border-radius:50%;background:#fff;display:block}
.legal-bar{left:0;top:3424px;width:1200px;height:102px;background:#e8e8e8}
.legal{left:145px;top:3443px;font-size:9px;line-height:17px;color:#7a7a7a}
.maps{left:821px;top:3449px;font-size:9px;color:#7a7a7a;display:flex;align-items:center;gap:8px}
.maps b{font-size:11px;font-weight:400;color:#555}
</style>
</head>
<body>

<!-- header -->
<div class="abs topbar"></div>
<div class="abs site-tag retro">DIGITAL ADVERTISING</div>
<div class="abs navbar"></div>
<ul class="abs nav">
  <li>Home</li><li>About Us</li><li>Services</li><li>Blog</li><li>Contact Us</li>
</ul>
<svg class="abs badge" viewBox="0 0 184 154" aria-hidden="true">
  <path d="M2 0 H182 V112 L92 150 L2 112 Z" fill="#7a3fd0"/>
  <path d="M10 0 H174 V106 L92 141 L10 106 Z" fill="#0b0f1e"/>
</svg>
<div class="abs badge-name">zQuandaro</div>

<div class="abs hero" role="img" aria-label="Blurred neon city lights background in violet, blue and pink"></div>
<div class="abs hero-title retro">RELEASE</div>
<div class="abs hero-sub">your ideas, products, and services to the world.</div>
<div class="abs hero-steps">visualize . plan . execute</div>

<!-- visualize -->
<section class="abs visualize">
  <div class="banner" style="position:relative">
    <div class="banner-photo" role="img" aria-label="Woman thinking beneath colourful gears and ideas"></div>
    <div class="banner-word retro" style="right:46px">VISUALIZE</div>
  </div>
  <div class="col-left">
    <p class="lede">zQuandaro verb pronounced <span>{z -kwan-dar-oh}</span>, or digital visionary is a person who uses the Internet as a global marketplace to release their ideas, products, and services to the world.</p>
    <p class="copy">They see the digital era as an open opportunity for small business to compete with large corporations and WIN! They understand the value of digital marketing as a tool to connect people with their business.</p>
    <p class="copy">Do you see yourself as a digital visionary? I'm here to coach you through the process of upgrading your imagination and mental thought process to connect your vision with business goals.</p>
  </div>
  <div class="col-right">
    <ul class="ticks vis-list">
      <li>Outlines on where to start the 5 year goal, downward</li>
      <li>Outlines on how to make sure your vision is clear</li>
      <li>How to start a Vision board</li>
      <li>Meditation tips</li>
      <li>Visionary Daily Routine tips</li>
      <li>Visionary Morning Routine tips</li>
      <li>How to create a vision for all areas of your life</li>
      <li>How God help lead your vision</li>
      <li>What a Godly imagination is</li>
      <li>Creating clear timelines</li>
      <li class="wrap">Creating Clear define goals, down to amount of clients and mount of revenue</li>
      <li>How is your vision helping others?</li>
      <li>Downloadable Habit tracker</li>
    </ul>
  </div>
</section>

<!-- plan -->
<section class="abs plan">
  <div class="banner">
    <div class="banner-photo" role="img" aria-label="Hands typing on a laptop showing a sales funnel beside coffee and glasses"></div>
    <div class="banner-word retro">PLAN</div>
  </div>
  <div class="col-left">
    <h2>Creating <b>digital sales funnel</b> for your business is key to your online growth.</h2>
    <p class="copy">Each channel should work cohesively together to reach your target audience. The placement of your ads and content you share is all part of the customer journey that you are creating for your business. My planning support is centered around your overall goals and the actions you want your customer to take.</p>
    <h2>View my planning resources and services here:</h2>
    <ul class="ticks resource-grid">
      <li>Paid Advertising (SEM)</li><li>Strategic Content creation (SEO)</li>
      <li>Email Marketing</li><li>Social Media</li>
      <li>Paid Social Media Advertising</li><li>Digital/Local Public Relations</li>
      <li>VidStream Advertising</li><li>Market specific Landing pages</li>
      <li>Shopzon</li>
    </ul>
  </div>
  <div class="col-right">
    <ul class="ticks plan-list">
      <li>How to create a marketing budget</li>
      <li>Best planning tools</li>
      <li>Planning your keywords</li>
      <li>How to find the best channels for your industry</li>
      <li>What is the digital Sales Funnel</li>
      <li>What is the difference between SEO and SEM</li>
      <li>How to plan for business operations</li>
      <li>Downloadable Social Media planner</li>
      <li>How to plan your ad schedule for paid advertising</li>
      <li>Defining your conversion goals</li>
      <li>How to plan a digital proposal</li>
      <li>How to set your ideal Geo-Targeting</li>
    </ul>
  </div>
</section>

<!-- execute -->
<section class="abs execute">
  <div class="banner">
    <div class="banner-photo" role="img" aria-label="Laptop with chalkboard sketch of ranking, SEO, content and keywords"></div>
    <div class="banner-word retro">EXECUTE</div>
  </div>
  <div class="col-left">
    <h2>Now that your plan is in place let's get ready to implement.</h2>
    <p class="copy">Creating a campaign should be geared around conversion goals that were put in place during the planning stage. Ad design and targeting should flow with a clear message defined for your unique audience.</p>
    <p class="copy">After launch the real work begins, continuous optimization is needed to improve overall campaign performance.</p>
    <div class="cta">CONTACT ME FOR MORE INFORMATION
      <svg width="10" height="12" viewBox="0 0 10 12" aria-hidden="true"><path d="M2 1 L7 6 L2 11" fill="none" stroke="#000205" stroke-width="2"/></svg>
    </div>
  </div>
  <div class="col-right">
    <ul class="ticks exe-list">
      <li>Design tools for beginners</li>
      <li>Landing page essentials guide</li>
      <li>Conversion focus Campaign Set-Up</li>
      <li>What you should look for in an agency</li>
      <li>Searchly Campaign types</li>
      <li>Optimization Tips for Display Campaigns</li>
    </ul>
  </div>
</section>

<!-- mission & purpose -->
<section class="abs mission">
  <div class="statement mission-box"><div class="frame">
    <h3>MISSION:</h3>
    <p>Be a valuable resource in my industry, that produces profitable results.</p>
  </div></div>
  <div class="statement purpose-box"><div class="frame">
    <h3>PURPOSE:</h3>
    <p>To fulfill the vision God gave me to assist Him in the creation of digital visionaries throughout the world.</p>
  </div></div>
</section>

<!-- partners -->
<section class="abs partners">
  <div class="brand" style="left:41px;top:38px"><span class="dot"></span><span>Searchly<br>Analytics</span></div>
  <div class="dashboard" role="img" aria-label="Analytics dashboard screenshot with bar charts and ring graphs"></div>
  <div class="brand" style="left:584px;top:44px"><span>Searchly<br>Console</span></div>
  <div class="ad-badge" aria-label="Social advertising partner badge"></div>
  <div class="partner-copy" style="left:30px;top:150px;width:490px">
    <p>Campaign creation and management is an ongoing optimization for improvement. We make sure campaigns are performing optimally and will make necessary adjustments as the market changes.</p>
    <p>Business Planning including proposals, budgets, and geo-targeting. Keyword planning, and analysis. Channel overviews, social media and landing page recommendations. Tying everything together with performance and data measurability..</p>
  </div>
  <div class="partner-copy" style="left:605px;top:147px;width:300px">
    <p>We specialize in all things Searchly making sure we follow all best practices to get results. Searchly Search, Searchly Display, Retargeting, VidStream ads, Postly Ads and Mobile App campaigns.</p>
    <p>Friendbook Advertising included in our strategies for lead generation</p>
  </div>
</section>

<!-- share -->
<div class="abs share-title retro">SHARE THIS PAGE</div>
<div class="abs share-row">
  <span style="background:#3b5998"></span>
  <span style="background:#1da1f2"></span>
  <span style="background:#0077b5"></span>
  <span class="plus">+</span>
</div>

<!-- footer -->
<div class="abs footer"></div>
<div class="abs foot-name">zquandaro.test</div>
<div class="abs foot-steps">visualize . plan . execute</div>
<div class="abs quick-title">Quick Links</div>
<ul class="abs quick"><li>HOME</li><li>About Us</li><li>Services</li><li>Blog</li></ul>
<div class="abs news-label">Subscribe to our newsletter</div>
<div class="abs news-input"></div>
<div class="abs news-btn">Submit</div>
<div class="abs social"><span></span><span></span></div>
<div class="abs legal-bar"></div>
<div class="abs legal">©2020 zQuandaro, Ltd. - All Rights Reserved<br>Terms &amp; Conditions | Privacy Policy | Contact Us</div>
<div class="abs maps">Find us on Searchly Maps: <b>Searchly Maps</b></div>

</body>
</html>
```